POLITICAL CARD TO HAND OUT

A LITTLE LARGER THAN THE REGULAR BUSINESS CARD WITH THE ABOVE INFORMATION.

Industry/Entity Type

Business

Contact Information for Business Card

ELECT *DEAN HOLT* FOR JUSTICE OF THE PEACE PCT 6-EXPERIENCED LEADERSHIP- WITH MY PICTURE ON IT- PHONE 347-610-2853-MERIDIAN PRIMARY - EARLY VOTING FEB 18TH THRU FEB 28 AND ELECTION DAY IS MARCH 4TH, 2014- USE RED WHITE AND BLUE WITH SOME STARS.

Requirements
Must have
• A FIVE POINTED STAR ON EACH SIDE OF MY NAME

```html
<!DOCTYPE html>
<html lang="en">
<head>
<meta charset="utf-8">
<title>Dean Holt for Justice of the Peace Pct 6</title>
<link href="https://fonts.googleapis.com/css2?family=Alfa+Slab+One&display=swap" rel="stylesheet">
<style>
  :root {
    --navy: #1b2b5e;
    --star-blue: #1a5e9a;
    --red: #e3202a;
    --stripe-red: #c8141c;
    --white: #ffffff;
    --shadow: rgba(0, 0, 0, 0.45);
  }
  html, body {
    margin: 0;
    padding: 0;
    overflow: hidden;
    background: var(--white);
  }
  .card {
    position: relative;
    width: 1200px;
    height: 695px;
    overflow: hidden;
    background: var(--white);
    font-family: "Alfa Slab One", Georgia, serif;
  }
  .layer {
    position: absolute;
    inset: 0;
  }
  .star-field { z-index: 0; }
  .flag-wave { z-index: 2; }
  .star { fill: var(--star-blue); }
  .stripe { fill: var(--stripe-red); }
  .wave-white { fill: var(--white); }
  .candidate-photo {
    position: absolute;
    z-index: 1;
    left: 750px;
    top: 0;
    width: 370px;
    height: 490px;
    background: linear-gradient(180deg, #ece5d6 0%, #d8c7ab 22%, #c9a48c 40%, #3a2f2c 58%, #1e1a1a 100%);
    box-shadow: 8px 8px 14px rgba(0, 0, 0, 0.35);
  }
  .text {
    position: absolute;
    z-index: 3;
    margin: 0;
    white-space: nowrap;
    line-height: 1;
  }
  .name {
    left: 156px;
    top: 136px;
    font-size: 54px;
    color: var(--navy);
    text-shadow: 4px 4px 4px var(--shadow);
  }
  .name .name-star {
    color: var(--red);
    font-size: 58px;
    text-shadow: none;
  }
  .office {
    left: 112px;
    top: 214px;
    font-size: 34px;
    color: var(--red);
    text-shadow: 3px 3px 3px var(--shadow);
  }
  .slogan {
    left: 123px;
    top: 326px;
    font-size: 36px;
    color: var(--navy);
    text-shadow: 4px 4px 4px var(--shadow);
  }
  .phone {
    left: 244px;
    top: 383px;
    font-size: 34px;
    color: var(--navy);
    text-shadow: 4px 4px 4px var(--shadow);
  }
  .vote-info {
    position: absolute;
    z-index: 3;
    left: 560px;
    top: 490px;
    width: 610px;
    margin: 0;
    text-align: center;
  }
  .vote-line {
    display: block;
    font-size: 24px;
    line-height: 56px;
    color: var(--navy);
    text-shadow: 3px 3px 3px var(--shadow);
  }
</style>
</head>
<body>
<main class="card">
  <svg class="layer star-field" width="1200" height="695" viewBox="0 0 1200 695" aria-hidden="true">
    <defs>
      <polygon id="star-shape" points="0,-1 0.225,-0.309 0.951,-0.309 0.363,0.118 0.588,0.809 0,0.382 -0.588,0.809 -0.363,0.118 -0.951,-0.309 -0.225,-0.309"/>
    </defs>
    <use href="#star-shape" class="star" transform="translate(330 72) rotate(-8) scale(72)"/>
    <use href="#star-shape" class="star" transform="translate(665 78) rotate(10) scale(72)"/>
    <use href="#star-shape" class="star" transform="translate(52 300) rotate(-14) scale(62)"/>
    <use href="#star-shape" class="star" transform="translate(340 505) rotate(-4) scale(72)"/>
    <use href="#star-shape" class="star" transform="translate(640 495) rotate(12) scale(68)"/>
    <use href="#star-shape" class="star" transform="translate(30 505) rotate(-10) scale(70)"/>
    <use href="#star-shape" class="star" transform="translate(1150 140) rotate(8) scale(80)"/>
    <use href="#star-shape" class="star" transform="translate(1165 335) rotate(-6) scale(70)"/>
  </svg>

  <div class="candidate-photo" role="img" aria-label="Portrait of the candidate in a white cowboy hat, dark suit and patterned tie"></div>

  <svg class="layer flag-wave" width="1200" height="695" viewBox="0 0 1200 695" aria-hidden="true">
    <path class="wave-white" d="M0 552 C 340 585, 720 510, 1200 372 L1200 695 L0 695 Z"/>
    <path class="stripe" d="M39 594 C 360 612, 720 540, 1159 425 L1159 465 C 720 570, 360 638, 39 614 Z"/>
    <path class="stripe" d="M39 633 C 360 648, 730 590, 1159 510 L1159 560 C 730 622, 360 672, 39 650 Z"/>
    <path class="wave-white" d="M0 655 L1200 655 L1200 695 L0 695 Z"/>
  </svg>

  <h1 class="text name"><span class="name-star">★</span>DEAN HOLT<span class="name-star">★</span></h1>
  <p class="text office">FOR JUSTICE OF THE PEACE PCT 6</p>
  <p class="text slogan">EXPERIENCED LEADERSHIP</p>
  <p class="text phone">PHONE 347-610-2853</p>

  <p class="vote-info">
    <span class="vote-line">MERIDIAN PRIMARY</span>
    <span class="vote-line">EARLY VOTING FEB 18TH THRU FEB 28</span>
    <span class="vote-line">ELECTION DAY IS MARCH 4TH, 2014</span>
  </p>
</main>
</body>
</html>
```